3D instagram advertisement explaining function of mask

I need an infographic commercial for my instagram ad. The company is an online health product store, and one of our products are reusable N95 masks. I am looking for someone to use 3D images to show how my "Plume veil" functions and what benefits come out of it. All masks have cartoon graphics on them and are made up of silver ion technology. which helps kill all virus and bacteria and blocks 5G radiation.

Target Market(s)

everyone

Industry/Entity Type

Health And Wellness

Font styles to use
Serif

Requirements
Must have
• -graphic of the mask and showing how the mask filters out bacteria and viruses
-one slide must show how many have been bought
-Canadian company must be emphasized
-graphics showing how 5G radiation bounces away from head
-warning slide stating that "the second wave is coming" and we need to protect ourselves early
Nice to have
• professional look but still fun since the masks are all cartoon characters

```html
<!DOCTYPE html>
<html lang="en">
<head>
<meta charset="utf-8">
<title>Plume veil mask layers</title>
<link rel="stylesheet" href="https://fonts.googleapis.com/css2?family=Teko:wght@400;600&display=swap">
<style>
  :root {
    --bg-light: #ffffff;
    --bg-mid: #e2e2e2;
    --bg-dark: #bdbdbd;
    --ink: #1c1c1c;
    --layer-nonwoven: #bdbdbd;
    --layer-carbon: #4a4a4a;
    --layer-meltdown: #d6d6d6;
    --layer-cotton: #4d4d4d;
    --layer-skin: #f2f2f2;
  }
  html, body {
    margin: 0;
    padding: 0;
    overflow: hidden;
  }
  .ad-canvas {
    position: relative;
    width: 1200px;
    height: 675px;
    overflow: hidden;
    background: radial-gradient(ellipse 70% 65% at 50% 20%, var(--bg-light) 0%, var(--bg-mid) 50%, var(--bg-dark) 100%);
    font-family: "Teko", "Arial Narrow", sans-serif;
    color: var(--ink);
  }
  .headline {
    position: absolute;
    top: 35px;
    left: 0;
    width: 100%;
    margin: 0;
    text-align: center;
    font-weight: 600;
    font-size: 42px;
    line-height: 48px;
    letter-spacing: 1px;
    text-transform: uppercase;
  }
  .layer-stack {
    position: absolute;
    top: 0;
    left: 0;
  }
  .layer-label {
    position: absolute;
    top: 541px;
    width: 160px;
    margin: 0 0 0 -80px;
    text-align: center;
    font-weight: 400;
    font-size: 25px;
    line-height: 29px;
    text-transform: uppercase;
  }
</style>
</head>
<body>
<main class="ad-canvas">
  <h1 class="headline">Antibacterial, UV resistant, quick absorption and fast drying,<br>dust resistant, soft and comfortable for everyday wear</h1>

  <svg class="layer-stack" width="1200" height="675" viewBox="0 0 1200 675" aria-label="Seven mask layers shown side by side">
    <defs>
      <path id="mask-shape" d="M0,24 L0.6,5 Q1.5,-1 2.6,5 L3.2,18 Q25,17 45,13 Q60,11 72,14 L96.6,16 L97.2,2 Q98.5,-3 99.6,2 L100,24 L100,62 Q98,97 52,100 Q6,99 0,60 Z"/>
      <path id="inner-rim" d="M3.2,18 Q25,17 45,13 Q60,11 72,14 L96.6,16 L96.6,21 Q72,19 58,17 Q40,19 3.2,23 Z"/>
      <linearGradient id="print-art" x1="0" y1="0" x2="0" y2="1">
        <stop offset="0" stop-color="#111"/>
        <stop offset="0.25" stop-color="#1a3552"/>
        <stop offset="0.55" stop-color="#3d7fb0"/>
        <stop offset="0.85" stop-color="#14283d"/>
        <stop offset="1" stop-color="#0c0c0c"/>
      </linearGradient>
      <linearGradient id="ion-layer" x1="0" y1="0" x2="0" y2="1">
        <stop offset="0" stop-color="#6a6a6a"/>
        <stop offset="1" stop-color="#8c8c8c"/>
      </linearGradient>
      <linearGradient id="shade-side" x1="0" y1="0" x2="1" y2="0">
        <stop offset="0" stop-color="#000" stop-opacity="0.38"/>
        <stop offset="0.18" stop-color="#000" stop-opacity="0.08"/>
        <stop offset="0.5" stop-color="#fff" stop-opacity="0.12"/>
        <stop offset="0.82" stop-color="#000" stop-opacity="0.08"/>
        <stop offset="1" stop-color="#000" stop-opacity="0.38"/>
      </linearGradient>
      <linearGradient id="shade-depth" x1="0" y1="0" x2="0" y2="1">
        <stop offset="0" stop-color="#000" stop-opacity="0.12"/>
        <stop offset="0.45" stop-color="#000" stop-opacity="0"/>
        <stop offset="1" stop-color="#000" stop-opacity="0.25"/>
      </linearGradient>
      <g id="shading">
        <use href="#mask-shape" fill="url(#shade-side)"/>
        <use href="#mask-shape" fill="url(#shade-depth)"/>
        <use href="#inner-rim" fill="#000" fill-opacity="0.35"/>
      </g>
    </defs>

    <g role="img" aria-label="Outer mask layer printed with a cartoon character artwork in black and glowing blue" transform="translate(138,153) scale(1.06,3.53)">
      <use href="#mask-shape" fill="url(#print-art)"/>
      <use href="#shading"/>
    </g>
    <g role="img" aria-label="Silver ion layer with a black and white dotted texture" transform="translate(255,159) scale(1.29,3.41)">
      <use href="#mask-shape" fill="url(#ion-layer)"/>
      <use href="#shading"/>
    </g>
    <g transform="translate(400,169) scale(1.48,3.24)">
      <use href="#mask-shape" fill="var(--layer-nonwoven)"/>
      <use href="#shading"/>
    </g>
    <g transform="translate(566,178) scale(1.43,3.06)">
      <use href="#mask-shape" fill="var(--layer-carbon)"/>
      <use href="#shading"/>
    </g>
    <g transform="translate(714,184) scale(1.39,2.95)">
      <use href="#mask-shape" fill="var(--layer-meltdown)"/>
      <use href="#shading"/>
    </g>
    <g transform="translate(864,188) scale(1.48,2.86)">
      <use href="#mask-shape" fill="var(--layer-cotton)"/>
      <use href="#shading"/>
    </g>
    <g transform="translate(1014,194) scale(1.47,2.75)">
      <use href="#mask-shape" fill="var(--layer-skin)"/>
      <use href="#shading" opacity="0.6"/>
    </g>
  </svg>

  <p class="layer-label" style="left:177px">Silver ion<br>particles</p>
  <p class="layer-label" style="left:317px">Silver ion<br>particles</p>
  <p class="layer-label" style="left:474px">Non woven</p>
  <p class="layer-label" style="left:636px">Activated<br>carbon filter</p>
  <p class="layer-label" style="left:793px">Electrostatic<br>meltdown</p>
  <p class="layer-label" style="left:948px">High efficiency<br>cotton filter</p>
  <p class="layer-label" style="left:1088px">Skin<br>friendly</p>
</main>
</body>
</html>
```